table invoices in a modern format! (make it fun to look at!!)

Our has invoices that are shown to our clients. This is currently done in a normal table view, but its boring to look at and is not modern.
We would like to have a modern look and feel
it should ABSOLUTLY not be in table form.
Cards, graphs, pictures, whatever... should be fun and almost interactive.

the table file is how it current looks like.
the other two files were "ideas" to have a better representation
IT DOES NOT NEED TO LOOK LIKE THAT if you have a better idea please go for it.

secondary objective, the graphs/cards/whatever you design should be interactive, meaning I can "click on it" to pay a bill, or see more info.

Let me know if there are more questions!

```html
<!DOCTYPE html>
<html lang="en">
<head>
<meta charset="utf-8">
<title>Invoices by Month</title>
<link rel="stylesheet" href="https://fonts.googleapis.com/css2?family=Arimo:wght@400;500&family=Montserrat:wght@500&family=Source+Code+Pro:wght@400;500&display=swap">
<style>
  :root {
    --page: #ffffff;
    --band-top: #9b86f5;
    --band-bottom: #70c8f7;
    --panel: #fdfdfd;
    --tab-bg: #f5f6f8;
    --tab-active: #26314a;
    --ink: #2a2d36;
    --muted: #5f6670;
    --cyan: #00bcd8;
    --blue: #0a5cf5;
    --green: #1a8a1a;
    --purple: #8a6ee0;
    --teal: #3fc8d6;
    --pink: #e2508f;
    --red-top: #9a2226;
    --red-mid: #9b1228;
    --red-low: #881236;
    --slate-top: #494a5f;
    --slate-low: #282a3e;
  }
  * { margin: 0; padding: 0; box-sizing: border-box; }
  html, body { width: 1200px; height: 1200px; overflow: hidden; background: var(--page); }
  body { position: relative; font-family: "Arimo", Arial, sans-serif; color: var(--ink); }

  .backdrop {
    position: absolute; left: 0; top: 152px; width: 1200px; height: 898px;
    background: linear-gradient(180deg, var(--band-top), var(--band-bottom));
  }
  .panel {
    position: absolute; left: 24px; top: 196px; width: 1146px; height: 829px;
    background: var(--panel); border-radius: 26px;
  }

  .year-tabs {
    position: absolute; left: 66px; top: 232px; height: 42px; width: 404px;
    display: flex; background: var(--tab-bg); border-radius: 3px; overflow: hidden;
  }
  .year-tab {
    width: 81px; display: flex; align-items: center; justify-content: center;
    font-size: 15px; color: var(--ink);
  }
  .year-tab.is-active { background: var(--tab-active); color: #fff; font-weight: 500; }

  .btn {
    position: absolute; display: flex; align-items: center; justify-content: center;
    color: #fff; font-size: 16px; border-radius: 3px;
  }
  .btn-overview { left: 948px; top: 242px; width: 160px; height: 42px; background: var(--cyan); }
  .btn-wallet { left: 651px; top: 312px; width: 159px; height: 45px; background: var(--blue); }

  .stat-icon {
    position: absolute; width: 44px; height: 44px; border-radius: 50%;
    display: flex; align-items: center; justify-content: center; background: #fff;
  }
  .stat-label {
    position: absolute; font-family: "Montserrat", sans-serif; font-size: 12px;
    letter-spacing: 2px; color: var(--ink);
  }
  .stat-value { position: absolute; font-size: 20px; color: var(--muted); }
  .stat-value.is-positive { color: var(--green); font-size: 18px; }

  .month-card {
    position: absolute; width: 237px; height: 239px; border-radius: 24px; overflow: hidden;
  }
  .month-card.is-past {
    background: linear-gradient(175deg, var(--red-top) 0%, var(--red-mid) 55%, var(--red-low) 100%);
    box-shadow: 0 4px 14px rgba(200, 40, 50, 0.35);
  }
  .month-card.is-upcoming {
    background: linear-gradient(180deg, var(--slate-top), var(--slate-low));
    box-shadow: 0 4px 12px rgba(40, 42, 62, 0.3);
  }
  .month-name {
    position: absolute; left: 0; right: 0; top: 11px; text-align: center;
    font-family: "Source Code Pro", monospace; font-size: 15px; font-weight: 400;
    letter-spacing: 3.5px; color: #fff;
  }
  .month-divider {
    position: absolute; left: 0; right: 0; top: 41px; height: 1px; background: rgba(255,255,255,0.25);
  }
  .is-upcoming .month-divider { left: 12px; top: 49px; }
  .badge-current {
    position: absolute; left: 178px; top: 33px; width: 30px; height: 7px; border-radius: 4px;
    background: #fff; color: var(--ink); font-size: 5px; letter-spacing: 0.5px;
    display: flex; align-items: center; justify-content: center;
  }
</style>
</head>
<body>
  <div class="backdrop"></div>
  <main class="panel"></main>

  <nav class="year-tabs">
    <span class="year-tab is-active">2019</span>
    <span class="year-tab">2020</span>
    <span class="year-tab">2021</span>
    <span class="year-tab">2022</span>
    <span class="year-tab">2023</span>
  </nav>
  <a class="btn btn-overview">Year Overview</a>

  <div class="stat-icon" style="left:77px;top:313px;border:1px solid #d9cff5;">
    <svg width="26" height="26" viewBox="0 0 26 26" fill="none" stroke="var(--purple)" stroke-width="1.5">
      <rect x="3" y="10" width="20" height="13" rx="1"/>
      <path d="M3 11l10 7 10-7M3 23l7-6M23 23l-7-6"/>
      <rect x="8" y="3" width="10" height="11" fill="#fff"/>
      <text x="13" y="12" font-size="8" text-anchor="middle" fill="var(--purple)" stroke="none">$</text>
    </svg>
  </div>
  <span class="stat-label" style="left:166px;top:316px;">PAYMENT</span>
  <span class="stat-value" style="left:144px;top:329px;">€ 10651.94</span>

  <div class="stat-icon" style="left:281px;top:313px;border:1px solid #c9eef2;">
    <svg width="24" height="26" viewBox="0 0 24 26" fill="none" stroke="var(--teal)" stroke-width="1.5">
      <path d="M4 2h16v21l-2-1.5-2 1.5-2-1.5-2 1.5-2-1.5-2 1.5-2-1.5-2 1.5z"/>
      <path d="M7 8h5M7 12h5M7 16h5"/>
      <text x="16" y="15" font-size="9" text-anchor="middle" fill="var(--teal)" stroke="none">$</text>
    </svg>
  </div>
  <span class="stat-label" style="left:353px;top:313px;">TOTAL PRICE</span>
  <span class="stat-value" style="left:348px;top:329px;">€ 7849.08</span>

  <div class="stat-icon" style="left:473px;top:313px;border:1px solid #f5cfe0;">
    <svg width="26" height="24" viewBox="0 0 26 24" fill="none" stroke="var(--pink)" stroke-width="1.5">
      <path d="M4 7l12-4 2 4"/>
      <rect x="2" y="7" width="21" height="14" rx="2"/>
      <path d="M23 11h-5v6h5"/>
      <text x="10" y="18" font-size="9" text-anchor="middle" fill="var(--pink)" stroke="none">$</text>
    </svg>
  </div>
  <span class="stat-label" style="left:540px;top:312px;">BALANCE</span>
  <span class="stat-value is-positive" style="left:540px;top:328px;">2802.86</span>
  <svg style="position:absolute;left:618px;top:330px;" width="18" height="18" viewBox="0 0 18 18">
    <path d="M8 2a7 7 0 1 0 7 8H8z" fill="#8a8d93"/>
    <path d="M10 0v8h8a8 8 0 0 0-8-8z" fill="#8a8d93"/>
  </svg>
  <a class="btn btn-wallet">Move To Wallet</a>

  <section class="month-card is-past" style="left:65px;top:452px;">
    <h2 class="month-name">JANUARY</h2><div class="month-divider"></div>
  </section>
  <section class="month-card is-past" style="left:334px;top:452px;">
    <h2 class="month-name">FEBRUARY</h2><div class="month-divider"></div>
    <span class="badge-current">ACTUAL</span>
  </section>
  <section class="month-card is-past" style="left:599px;top:452px;">
    <h2 class="month-name">MARCH</h2><div class="month-divider"></div>
  </section>
  <section class="month-card is-past" style="left:873px;top:452px;">
    <h2 class="month-name">APRIL</h2><div class="month-divider"></div>
  </section>

  <section class="month-card is-upcoming" style="left:62px;top:734px;">
    <h2 class="month-name">MAY</h2><div class="month-divider"></div>
  </section>
  <section class="month-card is-upcoming" style="left:332px;top:734px;">
    <h2 class="month-name">JUNE</h2><div class="month-divider"></div>
  </section>
  <section class="month-card is-upcoming" style="left:597px;top:734px;">
    <h2 class="month-name">JULY</h2><div class="month-divider"></div>
  </section>
  <section class="month-card is-upcoming" style="left:870px;top:734px;">
    <h2 class="month-name">AUGUST</h2><div class="month-divider"></div>
  </section>
</body>
</html>
```